Popup Banners - BrightCounsel - Legal Technology

- We need two banners (same style) designed with two different images and different text.

- The details of the printing requirements are attached, along with suggested images.

- The banners should share the same theme as our website www.brightcounsel.com.au

- The first banner would include our logo (attached), use the 'roads join' image (attached) in some way and text: New Opportunities - Where legal services and technology meet.

- The second banner would include our logo (attached), use the 'jigsaw' image (attached) in some way and use text: Legal Technology Strategy, Advice and Capability.

- Details on what are required from the Printer is attached also.

Target Market(s)

Legal Professionals

Industry/Entity Type

Information Technology

Font styles to use
Sans Serif

Requirements
Must have
• Our logo (attached), suggested text and the image mentioned for each.
Nice to have
• Professional and modern look
Should not have
• Cheap looking

```html
<!DOCTYPE html>
<html lang="en">
<head>
<meta charset="utf-8">
<title>BrightCounsel Popup Banners</title>
<link href="https://fonts.googleapis.com/css2?family=Josefin+Sans:wght@300;400&display=swap" rel="stylesheet">
<style>
  :root {
    --page: #ffffff;
    --trim: #e04848;
    --ink-dark: #4a4a4a;
    --ink-light: #ffffff;
    --sky-top: #a9c9ee;
    --sky-low: #c2daf2;
    --field-sky: #3f86c8;
    --field-green: #4e9a2c;
    --field-deep: #2f6a1c;
    --grass-band: rgba(44, 58, 38, 0.92);
    --grass-low: #5f8f3a;
    --puzzle-top: #8fb0d8;
    --puzzle-mid: #1d3150;
    --puzzle-glow: #c9e3ff;
    --slate-band: #2c3034;
    --puzzle-low: #5d86c2;
    --strip: rgba(255, 255, 255, 0.18);
  }
  * { box-sizing: border-box; margin: 0; padding: 0; }
  html, body { width: 1200px; height: 1200px; overflow: hidden; background: var(--page); }
  body { position: relative; font-family: "Josefin Sans", "Helvetica Neue", Arial, sans-serif; }

  .banner {
    position: absolute;
    top: 22px;
    width: 470px;
    height: 1156px;
    border: 1px solid var(--trim);
    overflow: hidden;
  }
  .banner--roads { left: 86px; }
  .banner--jigsaw { left: 645px; }

  .banner__section { position: absolute; left: 0; width: 100%; }
  .banner__head { top: 0; height: 204px; }
  .banner__photo { top: 204px; height: 312px; }
  .banner__band { top: 516px; height: 308px; }
  .banner__foot { top: 824px; height: 304px; }
  .banner__strip { top: 1128px; height: 28px; background: var(--strip); }

  .banner--roads .banner__head { background: linear-gradient(180deg, var(--sky-top), var(--sky-low)); }
  .banner--roads .banner__photo { background: linear-gradient(180deg, var(--field-sky) 0%, var(--field-sky) 18%, var(--field-green) 22%, var(--field-deep) 100%); }
  .banner--roads .banner__band { background: var(--grass-band); }
  .banner--roads .banner__foot { background: linear-gradient(180deg, var(--field-green), var(--grass-low) 60%, #6f9a48); }
  .banner--roads .banner__strip { background: #8fae6a; }

  .banner--jigsaw .banner__head { background: linear-gradient(180deg, var(--puzzle-top), #a6c0e2); }
  .banner--jigsaw .banner__photo { background: radial-gradient(circle at 52% 45%, var(--puzzle-glow) 0%, #5f87bd 22%, var(--puzzle-mid) 60%, #14233a 100%); }
  .banner--jigsaw .banner__band { background: var(--slate-band); }
  .banner--jigsaw .banner__foot { background: radial-gradient(circle at 60% 20%, #d7ebff 0%, #8fb2e0 30%, var(--puzzle-low) 75%, #4b70aa 100%); }
  .banner--jigsaw .banner__strip { background: #7d9fcf; }

  .wordmark {
    position: absolute;
    left: 0; width: 100%;
    text-align: center;
    font-weight: 400;
    letter-spacing: 0.2em;
    white-space: nowrap;
  }
  .wordmark--top { top: 146px; font-size: 38px; }
  .wordmark--bottom { top: 1042px; font-size: 28px; color: var(--ink-light); }
  .banner--roads .wordmark--top { color: var(--ink-dark); }
  .banner--jigsaw .wordmark--top { color: var(--ink-light); }

  .headline {
    position: absolute;
    left: 0; width: 100%;
    text-align: center;
    color: var(--ink-light);
    font-weight: 300;
    font-variant: small-caps;
    white-space: nowrap;
  }
  .headline--title { font-size: 29px; letter-spacing: 0.16em; }
  .headline--sub { font-size: 15px; letter-spacing: 0.2em; }
  .banner--roads .headline--title { top: 532px; }
  .banner--roads .headline--sub { top: 568px; }
  .banner--jigsaw .line-one { top: 530px; }
  .banner--jigsaw .line-two { top: 565px; }

  .service-icons { position: absolute; left: 0; top: 620px; width: 470px; height: 170px; }

  .service-label {
    position: absolute;
    color: var(--ink-light);
    font-size: 13px;
    font-weight: 300;
    font-variant: small-caps;
    letter-spacing: 0.18em;
    text-align: center;
    line-height: 17px;
    white-space: nowrap;
  }
  .banner--roads .service-label { left: 0; width: 100%; top: 794px; }
  .label--strategy { left: 27px; width: 160px; top: 780px; }
  .label--advice { left: 174px; width: 120px; top: 780px; }
  .label--capability { left: 303px; width: 120px; top: 780px; }

  .service-icons circle.ring,
  .service-icons .glyph { fill: none; stroke: var(--ink-light); stroke-width: 2; stroke-linecap: round; stroke-linejoin: round; }
</style>
</head>
<body>

<section class="banner banner--roads">
  <div class="banner__section banner__head"></div>
  <div class="banner__section banner__photo" role="img" aria-label="Photo of two dirt roads joining on a green grassy hill under a blue sky"></div>
  <div class="banner__section banner__band" role="img" aria-label="Close-up of green grass behind a dark translucent band"></div>
  <div class="banner__section banner__foot" role="img" aria-label="Close-up of long green grass"></div>
  <div class="banner__section banner__strip"></div>

  <div class="wordmark wordmark--top">BrightCounsel</div>

  <h1 class="headline headline--title">New Opportunities</h1>
  <p class="headline headline--sub">Where legal services and technology meet.</p>

  <svg class="service-icons" viewBox="0 0 470 170" aria-hidden="true">
    <circle class="ring" cx="173" cy="83" r="70"/>
    <circle class="ring" cx="298" cy="83" r="70"/>
    <!-- gavel -->
    <g class="glyph">
      <rect x="145" y="45" width="34" height="16" rx="3" transform="rotate(35 162 53)"/>
      <line x1="168" y1="62" x2="196" y2="88"/>
      <rect x="129" y="98" width="34" height="8" rx="2"/>
    </g>
    <!-- gears and laptop -->
    <g class="glyph">
      <circle cx="290" cy="46" r="14"/>
      <circle cx="290" cy="46" r="6"/>
      <circle cx="266" cy="78" r="9"/>
      <circle cx="283" cy="80" r="6"/>
      <path d="M282 62 H318 V98"/>
      <rect x="276" y="98" width="50" height="7" rx="2"/>
    </g>
  </svg>
  <p class="service-label">Legal Services + Technology</p>

  <div class="wordmark wordmark--bottom">BrightCounsel</div>
</section>

<section class="banner banner--jigsaw">
  <div class="banner__section banner__head" role="img" aria-label="Light blue jigsaw puzzle surface with a reaching hand"></div>
  <div class="banner__section banner__photo" role="img" aria-label="Photo of a hand placing a glowing jigsaw puzzle piece"></div>
  <div class="banner__section banner__band"></div>
  <div class="banner__section banner__foot" role="img" aria-label="Close-up of glowing jigsaw puzzle piece edges in blue"></div>
  <div class="banner__section banner__strip"></div>

  <div class="wordmark wordmark--top">BrightCounsel</div>

  <h1 class="headline headline--title line-one">Legal Technology Strategy,</h1>
  <p class="headline headline--title line-two">Advice and Capability.</p>

  <svg class="service-icons" viewBox="0 0 470 170" aria-hidden="true">
    <circle class="ring" cx="107" cy="82" r="70"/>
    <circle class="ring" cx="234" cy="82" r="70"/>
    <circle class="ring" cx="363" cy="82" r="70"/>
    <!-- strategy: gear and laptop -->
    <g class="glyph">
      <circle cx="93" cy="48" r="12"/>
      <circle cx="93" cy="48" r="5"/>
      <path d="M76 66 V100 M108 66 H134 V100"/>
      <rect x="70" y="100" width="70" height="7" rx="2"/>
    </g>
    <!-- advice: person and speech bubble -->
    <g class="glyph">
      <circle cx="222" cy="58" r="13"/>
      <path d="M198 106 V92 Q198 78 212 76 L222 88 L232 76 Q246 78 246 92 V106 Z"/>
      <path d="M242 44 H268 Q276 44 276 52 V58 Q276 66 268 66 H250 L242 72 Z"/>
    </g>
    <!-- capability: chain links -->
    <g class="glyph">
      <rect x="338" y="44" width="22" height="40" rx="11" transform="rotate(-40 349 64)"/>
      <rect x="366" y="78" width="22" height="40" rx="11" transform="rotate(-40 377 98)"/>
    </g>
  </svg>
  <p class="service-label label--strategy">Legal Technology<br>Strategy</p>
  <p class="service-label label--advice">Advice</p>
  <p class="service-label label--capability">Capability</p>

  <div class="wordmark wordmark--bottom">BrightCounsel</div>
</section>

</body>
</html>
```